Investor Information Presentation Design Required and Corporate overview design

I have all the materials ready to go, just need 1x Pro Design for the presentation and 1x Pro Design for the corporate overview.
I am ok with images being changed (only if it represents the company better). Wording Can NOT be changed. Any process diagrams can be changed to better represent the process.
I can provide high res Logo file and obviously the files for the presentation and corporate overview. What I have done is basic, but need it to look far more polished and professional.

Target Market(s)

Fixed Term Deposits - $100,000 + High interest rates

Industry/Entity Type

Investment

Font styles to use
Sans Serif

Requirements
Must have
• A corporate professional look, think banks, financial services, business etc
• The presentation is NOT used for group presenting purposes - Individuals go through it on their own. Should want to make me feel like I have to read it all!

```html
<!DOCTYPE html>
<html lang="en">
<head>
<meta charset="utf-8">
<title>Term Deposit Presentation – Layout Options</title>
<link rel="stylesheet" href="https://fonts.googleapis.com/css2?family=Arimo:wght@700&family=PT+Sans:wght@400;700&display=swap">
<style>
  :root {
    --page: #e6e6e6;
    --ink: #111111;
    --text: #2b2b2b;
    --blue: #1f78d1;
    --blue-dark: #1a63b0;
    --white: #ffffff;
    --rule: #c9c9c9;
    --clock-light: #f2f2f2;
    --clock-mid: #b9b9b9;
    --clock-dark: #3c3c3c;
    --accent-red: #c0262c;
    --sky: #6e8fb8;
    --glass: #394f6b;
  }
  * { box-sizing: border-box; margin: 0; padding: 0; }
  html, body { width: 1200px; height: 1200px; overflow: hidden; }
  body { background: var(--page); font-family: "PT Sans", sans-serif; color: var(--text); position: relative; }

  .divider { position: absolute; left: 0; width: 1200px; height: 6px; background: var(--ink); }
  .option-number { position: absolute; left: 60px; width: 140px; text-align: center; font-family: "Arimo", sans-serif; font-weight: 700; font-size: 196px; line-height: 1; color: var(--ink); }

  .slide { position: absolute; width: 393px; height: 221px; background: var(--white); overflow: hidden; box-shadow: 0 2px 4px rgba(0,0,0,.3); }
  .slide.left { left: 274px; }
  .slide.right { left: 751px; }

  .photo-clock { background: radial-gradient(circle at 55% 75%, var(--clock-light) 0 30%, var(--clock-mid) 48%, var(--clock-dark) 60%, #d8d8d8 72%, var(--clock-light) 100%); }
  .photo-clock::after { content: ""; position: absolute; inset: 0; background: linear-gradient(160deg, rgba(192,38,44,.18), transparent 55%); }
  .photo-building { background: linear-gradient(180deg, var(--sky) 0%, #9fb4cf 35%, var(--glass) 60%, #6c6f73 85%, #8a5a3e 100%); }
  .photo { position: absolute; }

  .title { color: var(--blue); font-weight: 700; line-height: 1.1; }
  .caps { text-transform: uppercase; }
  .bullets { list-style: none; }
  .bullets li { position: relative; padding-left: 11px; line-height: 1.3; }
  .bullets li::before { content: ""; position: absolute; left: 0; top: .45em; width: 4px; height: 4px; background: var(--blue); }
  .hl { color: var(--blue); font-weight: 700; }

  .brand { position: absolute; display: flex; flex-direction: column; align-items: center; gap: 2px; font-size: 5.5px; font-weight: 700; color: var(--glass); }
  .brand-mark { width: 9px; height: 9px; border-radius: 50%; background: var(--blue-dark); }

  .rates { border-collapse: collapse; text-align: center; }
  .rates th { font-weight: 700; }
  .rates .rate { color: var(--blue); }
  .notes { font-size: 3.6px; line-height: 1.35; color: #444; }
  .notes ul { padding-left: 6px; }
  .notes u { text-decoration: underline; }

  /* Option 1 */
  .o1 .photo { left: 0; top: 0; width: 393px; height: 81px; border-bottom: 1.5px solid var(--blue); }
  .o1 .title { position: absolute; left: 24px; top: 94px; font-size: 16px; }
  .o1 .bullets { position: absolute; left: 24px; top: 124px; font-size: 8.6px; }
  .o1 .bullets li { margin-bottom: 11px; }
  .o1 .brand { right: 8px; bottom: 14px; }
  .o1r .panel { position: absolute; left: 0; top: 0; width: 243px; height: 221px; border-right: 1.5px solid var(--blue); }
  .o1r .photo { left: 244px; top: 0; width: 149px; height: 221px; }
  .o1r .title { position: absolute; left: 18px; top: 20px; font-size: 14.5px; font-weight: 400; }
  .o1r .brand { left: 200px; top: 22px; }
  .o1r .rates { position: absolute; left: 18px; top: 74px; width: 212px; font-size: 5.5px; }
  .o1r .rates th { font-size: 6.5px; padding-bottom: 10px; vertical-align: bottom; }
  .o1r .rates th.rate { font-weight: 400; }
  .o1r .rates td { padding: 4px 0; }
  .o1r .rates td:first-child, .o1r .rates th:first-child { text-align: left; }
  .o1r .notes { position: absolute; left: 20px; top: 176px; width: 215px; }

  /* Option 2 */
  .o2 .photo, .o2r .photo { inset: 0; }
  .overlay-box { position: absolute; left: 26px; top: 32px; width: 340px; height: 164px; background: rgba(255,255,255,.86); border: 1.5px solid var(--blue); }
  .o2 .title { position: absolute; left: 19px; top: 16px; font-size: 17px; }
  .o2 .bullets { position: absolute; left: 19px; top: 52px; font-size: 8.6px; }
  .o2 .bullets li { margin-bottom: 11px; }
  .overlay-box .brand { right: 6px; bottom: 6px; }
  .o2r .title { position: absolute; left: 18px; top: 16px; font-size: 17px; font-weight: 400; }
  .o2r .overlay-box .brand { top: 8px; bottom: auto; right: 8px; }
  .o2r .rates { position: absolute; left: 18px; top: 48px; width: 236px; font-size: 7.6px; }
  .o2r .rates th { font-size: 7px; padding-bottom: 10px; vertical-align: bottom; }
  .o2r .rates th.rate { font-weight: 400; }
  .o2r .rates td { padding: 3px 0; }
  .o2r .notes { position: absolute; left: 266px; top: 72px; width: 68px; font-size: 3.3px; }

  /* Option 3 */
  .o3 .title { position: absolute; left: 20px; top: 36px; font-size: 17px; }
  .o3 .bullets { position: absolute; left: 20px; top: 72px; width: 150px; font-size: 7.2px; }
  .o3 .bullets li { margin-bottom: 8px; }
  .o3 .photo { left: 180px; top: 21px; width: 194px; height: 178px; border: 1.5px solid var(--blue); }
  .o3 .brand, .o3r .brand, .o4 .brand, .o4r .brand { left: 10px; bottom: 8px; }
  .o3r .title { position: absolute; left: 20px; top: 36px; font-size: 17px; }
  .o3r .rates { position: absolute; left: 19px; top: 72px; width: 223px; height: 106px; font-size: 6.8px; border: 1.5px solid var(--blue); }
  .o3r .rates th { background: var(--blue); color: var(--white); font-size: 7px; height: 29px; border-right: 2px solid var(--white); }
  .o3r .rates th:last-child { border-right: 0; }
  .o3r .rates td { border-right: 1.5px solid var(--blue); }
  .o3r .rates td:last-child { border-right: 0; font-weight: 700; }
  .o3r .rates .rate { color: var(--text); }
  .o3r .notes { position: absolute; left: 254px; top: 76px; width: 122px; font-size: 3.8px; }

  /* Option 4 */
  .o4 .title { position: absolute; left: 21px; top: 21px; font-size: 17px; }
  .o4 .bullets { position: absolute; left: 21px; top: 63px; width: 160px; font-size: 8.8px; }
  .o4 .bullets li { margin-bottom: 13px; }
  .o4 .photo-frame { position: absolute; left: 176px; top: 0; width: 217px; height: 221px; }
  .o4r .title { position: absolute; left: 21px; top: 21px; font-size: 17px; }
  .o4r .rates { position: absolute; left: 19px; top: 57px; width: 245px; height: 90px; font-size: 6.6px; border: 1.2px solid var(--blue); }
  .o4r .rates th { background: var(--blue); color: var(--white); font-size: 7px; height: 26px; border-right: 1.5px solid var(--white); }
  .o4r .rates th:last-child { border-right: 0; }
  .o4r .rates td { border-right: 1px solid var(--rule); }
  .o4r .rates td:last-child { border-right: 0; font-weight: 700; }
  .o4r .rates .rate { color: var(--text); }
  .o4r .notes { position: absolute; left: 20px; top: 154px; width: 258px; }
  .o4r .stripes { position: absolute; right: 0; top: 0; width: 393px; height: 221px; }
</style>
</head>
<body>

<div class="option-number" style="top:56px">1</div>
<div class="divider" style="top:289px"></div>
<div class="option-number" style="top:356px">2</div>
<div class="divider" style="top:589px"></div>
<div class="option-number" style="top:656px">3</div>
<div class="divider" style="top:889px"></div>
<div class="option-number" style="top:955px">4</div>

<!-- Option 1 -->
<section class="slide left o1" style="top:34px">
  <div class="photo photo-clock" role="img" aria-label="Close-up photo of a clock face reading 'Time to invest'"></div>
  <h2 class="title">The problem</h2>
  <ul class="bullets">
    <li>Term deposits with leading banks pay <span class="hl">less than 4.0% per annum</span></li>
    <li>Savings are getting <span class="hl">eroded by inflation</span></li>
    <li>Banks <span class="hl">continue to profit</span> despite paying low rates of return</li>
  </ul>
  <div class="brand"><span class="brand-mark"></span>Northvale Capital</div>
</section>

<section class="slide right o1r" style="top:34px">
  <div class="panel">
    <h2 class="title">Attractive Term<br>Deposits</h2>
    <div class="brand"><span class="brand-mark"></span>Northvale Capital</div>
    <table class="rates">
      <tr><th>Term</th><th>Investment<br>Size</th><th class="rate">Effective Annual<br>Interest rate</th></tr>
      <tr><td>3 months</td><td>$100k-$5m</td><td class="rate">5.95%</td></tr>
      <tr><td>6 months</td><td>$100k-$5m</td><td class="rate">6.40%</td></tr>
      <tr><td>12 months</td><td>$100k-$5m</td><td class="rate">6.95%</td></tr>
      <tr><td>24 months</td><td>$100k-$5m</td><td class="rate">7.40%</td></tr>
    </table>
    <div class="notes">Note:
      <ul>
        <li>Interest begins accruing from the day the funds arrive in the Northvale Capital bank account</li>
        <li>Each deposit is structured as a loan to Northvale Capital Pty Ltd per the terms of the Deposit Agreement</li>
        <li>Northvale Capital automatically deposits the <u>interest in your account each calendar quarter</u> on 1 January, 1 April, 1 July and 1 October</li>
        <li>Deposit Agreements automatically roll over for a further term unless the depositor provides no less than 14 days notice prior to the end of the deposit term should they wish to withdraw part or all of their principal</li>
      </ul>
    </div>
  </div>
  <div class="photo photo-building" role="img" aria-label="Photo of a modern glass office tower"></div>
</section>

<!-- Option 2 -->
<section class="slide left o2" style="top:334px">
  <div class="photo photo-clock" role="img" aria-label="Close-up photo of a clock face reading 'Time to invest'"></div>
  <div class="overlay-box">
    <h2 class="title">The problem</h2>
    <ul class="bullets">
      <li>Term deposits with leading banks pay <span class="hl">less than 4.0% per annum</span></li>
      <li>Savings are getting <span class="hl">eroded by inflation</span></li>
      <li>Banks <span class="hl">continue to profit</span> despite paying low rates of return</li>
    </ul>
    <div class="brand"><span class="brand-mark"></span>Northvale Capital</div>
  </div>
</section>

<section class="slide right o2r" style="top:334px">
  <div class="photo photo-building" role="img" aria-label="Photo of a modern glass office tower"></div>
  <div class="overlay-box">
    <h2 class="title">Attractive Term Deposits</h2>
    <div class="brand"><span class="brand-mark"></span>Northvale Capital</div>
    <table class="rates">
      <tr><th>Term</th><th>Investment<br>Size</th><th class="rate">Effective Annual<br>Interest rate</th></tr>
      <tr><td>3 months</td><td>$100k-$5m</td><td class="rate">5.95%</td></tr>
      <tr><td>6 months</td><td>$100k-$5m</td><td class="rate">6.40%</td></tr>
      <tr><td>12 months</td><td>$100k-$5m</td><td class="rate">6.95%</td></tr>
      <tr><td>24 months</td><td>$100k-$5m</td><td class="rate">7.40%</td></tr>
    </table>
    <div class="notes">Note:
      <ul>
        <li>Interest begins accruing from the day the funds arrive in the Northvale Capital bank account</li>
        <li>Each deposit is structured as a loan to Northvale Capital Pty Ltd per the terms of the Deposit Agreement</li>
        <li>Northvale Capital automatically deposits the <u>interest in your account each calendar quarter</u> on 1 January, 1 April, 1 July and 1 October</li>
        <li>Deposit Agreements automatically roll over for a further term unless the depositor provides no less than 14 days notice prior to the end of the deposit term should they wish to withdraw part or all of their principal</li>
      </ul>
    </div>
  </div>
</section>

<!-- Option 3 -->
<section class="slide left o3" style="top:634px">
  <h2 class="title caps">The problem</h2>
  <ul class="bullets">
    <li>Term deposits with leading banks pay <span class="hl">less than 4.0% per annum</span></li>
    <li>Savings are getting <span class="hl">eroded by inflation</span></li>
    <li>Banks <span class="hl">continue to profit</span> despite paying low rates of return</li>
  </ul>
  <div class="photo photo-clock" role="img" aria-label="Close-up photo of a clock face reading 'Time to invest'"></div>
  <div class="brand"><span class="brand-mark"></span>Northvale Capital</div>
</section>

<section class="slide right o3r" style="top:634px">
  <h2 class="title caps">Attractive Term Deposits</h2>
  <table class="rates">
    <tr><th>Term</th><th>Investment<br>Size</th><th>Effective Annual<br>Interest rate</th></tr>
    <tr><td>3 months</td><td>$100k-$5m</td><td class="rate">5.95%</td></tr>
    <tr><td>6 months</td><td>$100k-$5m</td><td class="rate">6.40%</td></tr>
    <tr><td>12 months</td><td>$100k-$5m</td><td class="rate">6.95%</td></tr>
    <tr><td>24 months</td><td>$100k-$5m</td><td class="rate">7.40%</td></tr>
  </table>
  <div class="notes">Note:
    <ul>
      <li>Interest begins accruing from the day the funds arrive in the Northvale Capital bank account</li>
      <li>Each deposit is structured as a loan to Northvale Capital Pty Ltd per the terms of the Deposit Agreement</li>
      <li>Northvale Capital automatically deposits the <u>interest in your account each calendar quarter</u> on 1 January, 1 April, 1 July and 1 October</li>
      <li>Deposit Agreements automatically roll over for a further term unless the depositor provides no less than 14 days notice prior to the end of the deposit term should they wish to withdraw part or all of their principal</li>
    </ul>
  </div>
  <div class="brand"><span class="brand-mark"></span>Northvale Capital</div>
</section>

<!-- Option 4 -->
<section class="slide left o4" style="top:933px">
  <h2 class="title caps">The problem</h2>
  <ul class="bullets">
    <li>Term deposits with leading banks pay <span class="hl">less than 4.0% per annum</span></li>
    <li>Savings are getting <span class="hl">eroded by inflation</span></li>
    <li>Banks <span class="hl">continue to profit</span> despite paying low rates of return</li>
  </ul>
  <svg class="photo-frame" viewBox="0 0 217 221" role="img" aria-label="Close-up photo of a clock face reading 'Time to invest', cut into angled panels">
    <defs>
      <radialGradient id="clockTone" cx="0.55" cy="0.75" r="0.8">
        <stop offset="0" stop-color="#f2f2f2"/>
        <stop offset="0.35" stop-color="#d6d6d6"/>
        <stop offset="0.55" stop-color="#4a4a4a"/>
        <stop offset="0.7" stop-color="#cfcfcf"/>
        <stop offset="1" stop-color="#f0f0f0"/>
      </radialGradient>
    </defs>
    <polygon points="0,0 217,0 217,221 40,221" fill="url(#clockTone)"/>
    <polygon points="0,0 217,0 217,221 40,221" fill="#c0262c" opacity="0.12"/>
    <line x1="96" y1="0" x2="122" y2="221" stroke="#ffffff" stroke-width="4"/>
    <line x1="152" y1="0" x2="178" y2="221" stroke="#ffffff" stroke-width="4"/>
  </svg>
  <div class="brand"><span class="brand-mark"></span>Northvale Capital</div>
</section>

<section class="slide right o4r" style="top:933px">
  <svg class="stripes" viewBox="0 0 393 221" aria-hidden="true">
    <polygon points="340,0 393,0 393,221 279,221" fill="#1f78d1"/>
    <polygon points="332,0 336,0 275,221 271,221" fill="#1f78d1"/>
  </svg>
  <h2 class="title caps">Attractive Term Deposits</h2>
  <table class="rates">
    <tr><th>Term</th><th>Investment<br>Size</th><th>Effective Annual<br>Interest rate</th></tr>
    <tr><td>3 months</td><td>$100k-$5m</td><td class="rate">5.95%</td></tr>
    <tr><td>6 months</td><td>$100k-$5m</td><td class="rate">6.40%</td></tr>
    <tr><td>12 months</td><td>$100k-$5m</td><td class="rate">6.95%</td></tr>
    <tr><td>24 months</td><td>$100k-$5m</td><td class="rate">7.40%</td></tr>
  </table>
  <div class="notes">Note:
    <ul>
      <li>Interest begins accruing from the day the funds arrive in the Northvale Capital bank account</li>
      <li>Each deposit is structured as a loan to Northvale Capital Pty Ltd per the terms of the Deposit Agreement</li>
      <li>Northvale Capital automatically deposits the <u>interest in your account each calendar quarter</u> on 1 January, 1 April, 1 July and 1 October</li>
      <li>Deposit Agreements automatically roll over for a further term unless the depositor provides no less than 14 days notice prior to the end of the deposit term should they wish to withdraw part or all of their principal</li>
    </ul>
  </div>
  <div class="brand"><span class="brand-mark"></span>Northvale Capital</div>
</section>

</body>
</html>
```